Argan Oil Shampoo/Conditioner Label

We are looking for 2 label designs. One for a shampoo bottle, and one for a conditioner bottle. The designs will be similar, however on the conditioner bottle, on the bottom of the label we would like a colored line across acting as a visual indicator to distinguish the two bottles.
Update - Brand name is being finalized but instead of essentials use "Meadow - Concept use a raindrop in place of the apostrophe. And smaller font for “Meadow” directly under “Tem’s”
As for the label, we are looking for a background design for the label as well as some concepts for the main product information and we will need to add the ingredients and instructions later.
Concepts for the Product label, the shampoo and conditioner is going to consist of Argan Oil, so having a black silhouette of an argan tree.
We don’t want something too extravagant or gaudy. Something simple but will make the product look high class. This will be a premium product and we want the label to portray that.
Update- The label dimensions are estimated to be 7.75" wrapped around the bottle. The height of the label will be estimated at 5" from top to bottom.
Please use your artistic minds, we are open to other ideas and concepts as well with keeping to the above mentioned restrictions of not being too gaudy and extravagant.
We are seeking some revisions from a designer and are wanting to give him some more time.

```html
<!DOCTYPE html>
<html lang="en">
<head>
<meta charset="utf-8">
<title>Tem’s Meadow – Shampoo &amp; Conditioner Labels</title>
<link rel="stylesheet" href="https://fonts.googleapis.com/css2?family=Lato:wght@400;700&family=Delius&display=swap">
<style>
  :root {
    --page: #e6e6e6;
    --label-white: #ffffff;
    --charcoal: #3b3b3c;
    --charcoal-soft: #464647;
    --orange: #ee5a24;
    --ink: #333333;
    --text-light: #f2f2f2;
  }
  * { margin: 0; padding: 0; box-sizing: border-box; }
  html, body { width: 1200px; height: 960px; overflow: hidden; background: var(--page); }
  .canvas {
    width: 1200px; height: 960px;
    display: flex; align-items: center; justify-content: center; gap: 20px;
  }
  .label { position: relative; width: 340px; height: 540px; overflow: hidden; box-shadow: 0 6px 18px rgba(0,0,0,.12); }
  .label-front { background: var(--label-white); }
  .label-art { position: absolute; inset: 0; }
  .brand {
    position: absolute; top: 120px; right: 20px; text-align: right;
    font-family: "Lato", sans-serif; font-weight: 400; color: var(--ink); line-height: 1;
  }
  .brand-name { font-size: 74px; display: flex; align-items: flex-start; justify-content: flex-end; gap: 6px; }
  .brand-dot { width: 14px; height: 14px; border-radius: 50%; background: var(--orange); margin-top: 12px; }
  .brand-sub { font-size: 46px; margin-top: 2px; }
  .product-name {
    position: absolute; left: 22px; bottom: 38px;
    font-family: "Delius", cursive; font-size: 38px; color: var(--orange); letter-spacing: 1px;
  }
  .label-back {
    width: 300px; background: var(--charcoal); color: var(--text-light);
    font-family: "Lato", sans-serif; text-align: center; padding-top: 58px;
  }
  .info-section { padding: 10px 0 12px; border-bottom: 2px solid var(--text-light); }
  .info-section:last-of-type { border-bottom: none; }
  .info-title { font-size: 17px; font-weight: 400; letter-spacing: .3px; margin-bottom: 8px; }
  .info-body { font-size: 10.5px; line-height: 1.35; padding: 0 8px; }
  .company { position: absolute; left: 12px; bottom: 96px; text-align: left; }
  .company-name { font-size: 13px; font-weight: 700; margin-bottom: 3px; }
  .company-address { font-size: 10px; line-height: 1.3; }
</style>
</head>
<body>
<main class="canvas">

  <section class="label label-front label-shampoo">
    <svg class="label-art" viewBox="0 0 340 540" width="340" height="540" aria-hidden="true">
      <path d="M0 205 C110 255 260 300 340 420 L340 442 C250 325 110 285 0 240 Z" fill="var(--orange)"/>
      <path d="M0 262 C110 312 250 350 340 460 L340 540 L0 540 Z" fill="var(--orange)"/>
      <path d="M0 276 C110 326 250 366 340 472 L340 540 L0 540 Z" fill="var(--charcoal)"/>
    </svg>
    <svg class="label-art" viewBox="0 0 340 540" width="340" height="540" role="img" aria-label="Faint argan tree silhouette">
      <ellipse cx="60" cy="410" rx="60" ry="55" fill="var(--charcoal-soft)"/>
    </svg>
    <div class="brand">
      <div class="brand-name">Tem’s<span class="brand-dot"></span></div>
      <div class="brand-sub">Meadow</div>
    </div>
    <div class="product-name">shampoo</div>
  </section>

  <section class="label label-back">
    <div class="info-section">
      <h2 class="info-title">OUR PHILOSOPHY</h2>
      <p class="info-body">Lorem ipsum dolor sit amet, consectetuer adipiscing elit, sed diam nonummy nibh euismod tincidunt ut laoreet dolore magna aliquam erat volutpat. Ut wisi enim ad minim veniam, quis nostrud exerci tation ullamcorper suscipit lobortis nisl ut aliquip ex ea commodo consequat.</p>
    </div>
    <div class="info-section">
      <h2 class="info-title">THIS PRODUCT</h2>
      <p class="info-body">Lorem ipsum dolor sit amet, consectetuer adipiscing elit, sed diam nonummy nibh euismod tincidunt ut laoreet dolore magna aliquam volutpat. Ut wisi enim ad minim veniam.</p>
    </div>
    <div class="info-section">
      <h2 class="info-title">OUR LEAD STYLIST SUGGESTS</h2>
      <p class="info-body">Lorem ipsum dolor sit amet, consectetuer adipiscing elit, sed diam nonummy nibh euismod tincidunt ut laoreet dolore magna aliquam volutpat. Ut wisi enim ad minim veniam, quis nostrud exerci tation ullamcorper suscipit lobortis nisl ut aliquip ex ea commodo consequat.</p>
    </div>
    <div class="company">
      <p class="company-name">Meadow private limited</p>
      <p class="company-address">Address here please, address here please<br>address here: Ph:000 0000 0000</p>
    </div>
  </section>

  <section class="label label-front label-conditioner">
    <svg class="label-art" viewBox="0 0 340 540" width="340" height="540" aria-hidden="true">
      <path d="M0 205 C110 255 260 300 340 420 L340 442 C250 325 110 285 0 240 Z" fill="var(--orange)"/>
      <path d="M0 262 C110 312 250 350 340 460 L340 540 L0 540 Z" fill="var(--orange)"/>
      <path d="M0 276 C110 326 250 366 340 472 L340 540 L0 540 Z" fill="var(--charcoal)"/>
    </svg>
    <svg class="label-art" viewBox="0 0 340 540" width="340" height="540" role="img" aria-label="Faint argan tree silhouette">
      <ellipse cx="40" cy="400" rx="50" ry="55" fill="var(--charcoal-soft)"/>
    </svg>
    <div class="brand">
      <div class="brand-name">Tem’s<span class="brand-dot"></span></div>
      <div class="brand-sub">Meadow</div>
    </div>
    <div class="product-name">conditioner</div>
  </section>

</main>
</body>
</html>
```